Steadfast MD - Sleep Medicine Specialist - Business Cards

We are a new medical practice called Steadfast MD. We are sleep medicine specialists and we will be conducting sleep studies on patients with sleep related ailments. We want the business card to be bold, professional, and clean with the logo as the stand out visual piece. We dont like wild flashy designs. We want our design to be bold and classic while at the same time conveying who we are and what we do. We are reliable, professional, and the best in the business.

Industry/Entity Type

Health Care

Contact Information for Business Card

- Clean
- Bold
- Classic
- not cluttered

Requirements
Must have
• logo, website, phone number
Nice to have
• several options to choose from
Should not have
• flashy imaged - reflective print - images of people sleeping

```html
<!DOCTYPE html>
<html lang="en">
<head>
<meta charset="utf-8">
<title>Steadfast MD – Business Card</title>
<link href="https://fonts.googleapis.com/css2?family=Arimo:wght@400;700&display=swap" rel="stylesheet">
<style>
  :root {
    --page-bg: #e4e2df;
    --card-dark: #121315;
    --card-dark-edge: #1d1f22;
    --card-light-a: #e9e4dc;
    --card-light-b: #cfd3d6;
    --accent-red: #d0111b;
    --text-light: #e6dccb;
    --logo-ink: #141414;
  }
  * { margin: 0; padding: 0; box-sizing: border-box; }
  html, body {
    width: 1200px; height: 897px; overflow: hidden;
    background: var(--page-bg);
    font-family: "Arimo", Arial, sans-serif;
  }
  .card {
    position: absolute; left: 100px; top: 175px;
    width: 1000px; height: 547px;
    border-radius: 26px; overflow: hidden;
    background: linear-gradient(135deg, var(--card-light-a), var(--card-light-b));
    box-shadow: 0 10px 30px rgba(0,0,0,0.18);
  }
  .card-shapes { position: absolute; inset: 0; }
  .accent-bar {
    position: absolute; left: 0; top: 95px;
    width: 20px; height: 63px; background: var(--accent-red);
  }
  .holder { position: absolute; left: 46px; top: 92px; }
  .holder-name {
    color: var(--accent-red); font-weight: 700; font-size: 37px;
    letter-spacing: 0.5px; line-height: 1;
  }
  .holder-title { color: var(--text-light); font-size: 22px; margin-top: 12px; }
  .address {
    position: absolute; left: 45px; top: 258px;
    color: var(--text-light); font-size: 22px; line-height: 34px;
  }
  .contacts { position: absolute; left: 42px; top: 388px; list-style: none; }
  .contacts li {
    display: flex; align-items: center; gap: 11px;
    color: var(--text-light); font-size: 22px; height: 37px;
  }
  .contact-icon {
    width: 24px; height: 24px; background: var(--accent-red);
    border-radius: 3px; display: flex; align-items: center; justify-content: center;
  }
  .brand {
    position: absolute; left: 580px; top: 225px;
    display: flex; align-items: center; gap: 14px;
  }
  .brand-mark {
    width: 90px; height: 90px; border-radius: 50%;
    border: 5px solid var(--accent-red);
  }
  .brand-name {
    color: var(--logo-ink); font-weight: 700; font-size: 40px; letter-spacing: -0.5px;
  }
</style>
</head>
<body>
  <div class="card">
    <svg class="card-shapes" width="1000" height="547" viewBox="0 0 1000 547" aria-hidden="true">
      <defs>
        <linearGradient id="darkPanel" x1="0" y1="0" x2="1" y2="1">
          <stop offset="0" stop-color="var(--card-dark-edge)"/>
          <stop offset="1" stop-color="var(--card-dark)"/>
        </linearGradient>
      </defs>
      <path d="M0,0 L625,0 Q420,273 643,547 L0,547 Z" fill="var(--accent-red)"/>
      <path d="M0,0 L613,0 Q408,273 630,547 L0,547 Z" fill="url(#darkPanel)"/>
    </svg>

    <div class="accent-bar"></div>
    <div class="holder">
      <div class="holder-name">DANIEL HAYES</div>
      <div class="holder-title">Doctor</div>
    </div>

    <div class="address">
      <div>1480 W Harbor Avenue</div>
      <div>Brookfield County Name 6418</div>
    </div>

    <ul class="contacts">
      <li>
        <span class="contact-icon">
          <svg width="14" height="14" viewBox="0 0 24 24" aria-hidden="true"><path fill="#fff" d="M6.6 10.8a15 15 0 0 0 6.6 6.6l2.2-2.2a1 1 0 0 1 1-.25 11.4 11.4 0 0 0 3.6.57 1 1 0 0 1 1 1V20a1 1 0 0 1-1 1A17 17 0 0 1 3 4a1 1 0 0 1 1-1h3.5a1 1 0 0 1 1 1c0 1.25.2 2.45.57 3.57a1 1 0 0 1-.25 1z"/></svg>
        </span>
        123-684-20517
      </li>
      <li>
        <span class="contact-icon">
          <svg width="15" height="12" viewBox="0 0 20 14" aria-hidden="true"><rect x="1" y="1" width="18" height="12" fill="none" stroke="#fff" stroke-width="2"/><path d="M1 1 L10 8 L19 1" fill="none" stroke="#fff" stroke-width="2"/></svg>
        </span>
        info@steadfastmd.com
      </li>
      <li>
        <span class="contact-icon">
          <svg width="15" height="15" viewBox="0 0 20 20" aria-hidden="true"><circle cx="10" cy="10" r="8" fill="none" stroke="#fff" stroke-width="2"/><path d="M2 10h16M10 2c3 3 3 13 0 16M10 2c-3 3-3 13 0 16" fill="none" stroke="#fff" stroke-width="1.5"/></svg>
        </span>
        www.steadfastmd.com
      </li>
    </ul>

    <div class="brand">
      <div class="brand-mark"></div>
      <div class="brand-name">Steadfast MD</div>
    </div>
  </div>
</body>
</html>
```